VENTRIX Hardware needs a Flyer Designed

We need a flyer designed for a marketing strategy that is to be launched by VENTRIX. As it is for our hardware division, our logo should go unto the flyer. We are offering to our customers financing on items from $5000 up to $35000. Here are some key words that you may want to include; "building or revovating? you pick the job we've got the financing." The flyer should reflect some sort of home construction and should be very attractive and vibrant. On the flyer it should also state that it's "hassle-free" and; "no down payment", "no collateral", "affordable monthly payments".

Must Haves [en ]: The companies logo. Also it must state the address of the company and contact info which is; 47 Bellweather Lane Penal, Trinidad. Tel: 868-55-VENTRIX. Email must also be listed: info@ventrixholdings.example.

Nice To Haves [en ]: Good quality graphics. something that is captivating and that will hold the attention of our audience.

Should Not Haves [en ]: Should not be too busy.

Industry/Entity Type

Marketing

Requirements
Must have
• The companies logo. Also it must state the address of the company and contact info which is; 47 Bellweather Lane Penal, Trinidad. Tel: 868-55-VENTRIX. Email must also be listed: info@ventrixholdings.example.
Nice to have
• Good quality graphics. something that is captivating and that will hold the attention of our audience.
Should not have
• Should not be too busy.

```html
<!DOCTYPE html>
<html lang="en">
<head>
<meta charset="utf-8">
<title>VENTRIX Hardware – Building or Renovating Flyer</title>
<link rel="stylesheet" href="https://fonts.googleapis.com/css2?family=Montserrat:wght@400;800&family=Arimo:ital,wght@0,400;0,700;1,400&display=swap">
<style>
  :root {
    --yellow-light: #fde686;
    --yellow: #f9d34a;
    --yellow-deep: #f5c227;
    --orange: #f6a31f;
    --orange-deep: #ee8b14;
    --red: #e0263f;
    --navy: #1d2a5b;
    --white: #ffffff;
    --grey-light: #f1f1f1;
    --grey: #c9c9c9;
  }
  * { margin: 0; padding: 0; box-sizing: border-box; }
  html, body {
    width: 1200px; height: 900px; overflow: hidden;
    background: var(--white);
  }
  .flyer {
    position: relative;
    width: 1200px; height: 900px;
    overflow: hidden;
    border: 6px solid var(--red);
    background: radial-gradient(ellipse at 45% 35%, var(--yellow-light) 0%, var(--yellow) 55%, var(--yellow-deep) 100%);
    font-family: "Arimo", Arial, sans-serif;
    color: var(--navy);
  }
  .headline {
    position: absolute; left: 72px; top: 70px;
    font-family: "Montserrat", Arial, sans-serif;
    line-height: 1;
    letter-spacing: -1px;
  }
  .headline__lead { display: block; font-weight: 400; font-size: 88px; color: var(--navy); }
  .headline__accent { display: block; font-weight: 800; font-size: 88px; color: var(--red); margin-top: 6px; }

  .brand-box {
    position: absolute; left: 792px; top: 0; width: 346px; height: 245px;
    background: var(--white);
    display: flex; flex-direction: column; align-items: center; justify-content: center;
  }
  .brand-box__name {
    display: flex; align-items: center; gap: 14px;
    font-family: "Montserrat", Arial, sans-serif; font-weight: 800;
    font-size: 56px; color: var(--navy); letter-spacing: 1px;
  }
  .brand-box__mark { width: 30px; height: 30px; background: var(--red); }
  .brand-box__rule { width: 270px; height: 2px; background: var(--navy); margin: 18px 0 8px; }
  .brand-box__group {
    font-family: "Arimo", Arial, sans-serif; font-size: 15px;
    letter-spacing: 1px; color: var(--navy);
  }

  .tagline-banner { position: absolute; left: 0; top: 298px; width: 716px; height: 150px; }
  .tagline-banner svg { position: absolute; inset: 0; }
  .tagline-banner__text {
    position: absolute; left: 72px; top: 28px;
    font-style: italic; font-size: 40px; line-height: 1.2; color: var(--navy);
  }

  .offer { position: absolute; left: 72px; top: 500px; font-size: 27px; }
  .offer__amount { font-weight: 700; color: var(--navy); }

  .benefits { position: absolute; left: 72px; top: 580px; list-style: none; font-size: 27px; }
  .benefits li { display: flex; align-items: center; gap: 16px; height: 47px; }
  .benefits svg { width: 20px; height: 20px; }

  .home-artwork {
    position: absolute; left: 700px; top: 380px; width: 488px; height: 508px;
    border-radius: 40px 0 0 0;
    background:
      radial-gradient(ellipse at 55% 30%, rgba(224,38,63,0.55) 0%, rgba(224,38,63,0) 38%),
      radial-gradient(ellipse at 55% 65%, var(--white) 0%, var(--grey-light) 45%, var(--grey) 100%);
    opacity: 0.95;
  }

  .contact-band { position: absolute; left: 0; bottom: 0; width: 700px; height: 150px; }
  .contact-band svg { position: absolute; inset: 0; }
  .contact-band__text {
    position: absolute; left: 72px; top: 42px;
    color: var(--white); font-size: 26px; line-height: 1.6;
  }
  .contact-band__phone { font-weight: 700; }
  .contact-band__divider { margin: 0 10px; }
</style>
</head>
<body>
<main class="flyer">
  <h1 class="headline">
    <span class="headline__lead">BUILDING OR</span>
    <span class="headline__accent">RENOVATING?</span>
  </h1>

  <div class="brand-box">
    <div class="brand-box__name"><span class="brand-box__mark"></span>VENTRIX</div>
    <div class="brand-box__rule"></div>
    <div class="brand-box__group">GROUP OF COMPANIES</div>
  </div>

  <div class="tagline-banner">
    <svg width="716" height="150" viewBox="0 0 716 150">
      <defs>
        <linearGradient id="bannerFill" x1="0" y1="0" x2="1" y2="0">
          <stop offset="0" stop-color="#f6a31f"/>
          <stop offset="1" stop-color="#f7b531"/>
        </linearGradient>
      </defs>
      <polygon points="0,0 640,0 716,150 0,150" fill="url(#bannerFill)"/>
    </svg>
    <p class="tagline-banner__text">YOU PICK THE JOB,<br>WE’VE GOT THE FINANCES!</p>
  </div>

  <p class="offer">Get up to <span class="offer__amount">$35,000.00</span> hassle-free at</p>

  <ul class="benefits">
    <li><svg viewBox="0 0 20 20"><path d="M2 11 L7 16 L18 3" fill="none" stroke="#1d2a5b" stroke-width="2.4"/></svg>No Down-payment</li>
    <li><svg viewBox="0 0 20 20"><path d="M2 11 L7 16 L18 3" fill="none" stroke="#1d2a5b" stroke-width="2.4"/></svg>No Collateral</li>
    <li><svg viewBox="0 0 20 20"><path d="M2 11 L7 16 L18 3" fill="none" stroke="#1d2a5b" stroke-width="2.4"/></svg>Affordable Monthly Payments</li>
  </ul>

  <div class="contact-band">
    <svg width="700" height="150" viewBox="0 0 700 150">
      <polygon points="0,0 640,0 700,150 0,150" fill="#e0263f"/>
    </svg>
    <p class="contact-band__text">
      47 Bellweather Lane Penal, Trinidad.<br>
      <span class="contact-band__phone">868-55-VENTRIX</span><span class="contact-band__divider">|</span>info@ventrixholdings.example
    </p>
  </div>

  <div class="home-artwork" role="img" aria-label="3D model house with a red tiled roof resting on rolled architectural blueprints"></div>
</main>
</body>
</html>
```